Software Product Brochure

tidewell is a new cloud based hotel management platform, this solution is our new offering to the hospitality vertical.The solution being cloud based, it is scalable, serving everyone from small Inns, bread & breakfast, hotels, service apartments and resorts to branded-chain operators. Our software is self configurable by hotel based on type of business and spans both guest facing and back office functions.

Hospitality Solution that enables Operational Excellence and widens Customer Reach

BELOW IS A SIMPLE BRIEF ON SOLUTION BUT ACTUAL CONTENT TO BE USED IN DESIGN AND BROCHURE MUST BE FROM THE ENCLOSED DOCUMENTS WITH THIS PROJECT.

A truly Integrated Solution
Manages Distributed Operational Work-flows
Inventory Distributions, Sales and Marketing
Strategic Planning /Reporting and Management

No Compromise, Cloud based solution – at affordable cost, low learning curve, requiring minimal Infrastructure

PMS at an affordable price

Easy to adapt and Simple to use, One platform can serve all of the brands within a chain

Same UI across all brands reduces training efforts

No Servers required, No Installation and Zero maintenance

Online wizard based Installation , reduces cost of setup & training.

Channel Manager- Centralized rates and Real Time inventory distribution

Travel Agents & Corporate logins with specific rates

Unlimited package & rates creations with date validations

Short Learning Curve, Improved Revenues & ROI

Data Security with 99.5% server uptime and Offline Report Availability

Anywhere anytime benefit

Tidewell helps by offering a more cost-effective alternative to on-premises applications. The major benefit that it offers is zero capital expense, lower cost of ownership, faster implementation, quicker training, and a quick return-on-investment are just some of the paybacks. Hotels only need to subscribe to the bandwidth through a reliable Internet ISP

The market is a mature market with many competitors. A few very well established with some good track record. This brochure is targeted at the global market. The target market is jaded with the number of options available. We will focus on small and mid size hotels with a hope that the product would excite them as the competitors offer very basic and more expensive solution whereas we offer a more feature rich and a growing platform.

We are hoping that the brochure will stand-out from the crowd and will compel the market to browse through what we do.

Some key competitors include -
http://www.gablerest.example
http://www.lodgetallypms.example
http://www.porchbellonline.example
http://www.stayvantix.example

We have a company and sample product brochure we made (both attached). We have also developed a web site (see www.tidewellstays.example). The brochure design need not conform to the web site, if (and only if) you can come up with a really attention seeking design (we could consider redesign of the web site).

The content of the brochure will largely conform to the sample brochure submitted because we have carefully taken the content out for the sample brochure.

——————
We also want below quote to be enclosed and highlighted some place in brochure in both versions

QUOTE START.....

"We travel a lot and want to be able to see how the occupancy is at anytime. We wanted a technology which could connect our HO to property and also help us manage multiple properties.

With tidewell adoption not only have we streamlined our operations but also seen a 20% jump in occupancy

Tomov –MD,
K-Lodging

QUOTE END
——————
Updates

I have a website www.tidewellstays.example. The theme and colour scheme of brochure must match this and both brochure designs should be slightly different. One is full spec brochure and other is a summary of same.

Target Market(s)

This is meant for hotels

Industry/Entity Type

Hospitality

Requirements
Must have
• Colour theme must match www.tidewellstays.example
Nice to have
• The design should be elegant and professional in appearance but playful and not very serious.
Should not have
• Weird colours or images with colours which do not go with my website theme.

```html
<!DOCTYPE html>
<html lang="en">
<head>
<meta charset="utf-8">
<title>tidewell – Hospitality Solution Brochure</title>
<link rel="stylesheet" href="https://fonts.googleapis.com/css2?family=Montserrat:wght@500;800&family=Open+Sans:wght@700&display=swap">
<style>
  :root {
    --brand-red: #c52009;
    --brand-blue: #0b87d9;
    --brand-orange: #f5921e;
    --photo-sky: #dbe7ef;
    --photo-blue: #4f7f9c;
    --photo-green: #4d7440;
    --photo-leaf: #79a050;
    --white: #ffffff;
  }
  * { margin: 0; padding: 0; box-sizing: border-box; }
  html, body { width: 849px; height: 1200px; overflow: hidden; background: var(--white); }
  .brochure { position: relative; width: 849px; height: 1200px; overflow: hidden; font-family: "Montserrat", sans-serif; }

  .hero-photo {
    position: absolute; left: 0; top: 0; width: 849px; height: 786px;
    background: linear-gradient(100deg, var(--photo-sky) 0%, #b9cfdc 18%, var(--photo-blue) 38%, #587a64 62%, var(--photo-green) 82%, var(--photo-leaf) 100%);
  }

  .brand {
    position: absolute; left: 58px; top: 96px;
    display: flex; align-items: center; gap: 12px;
  }
  .brand-dot { width: 22px; height: 22px; border-radius: 50%; background: var(--brand-blue); }
  .brand-name { font-weight: 800; font-size: 52px; color: var(--brand-red); letter-spacing: -1px; line-height: 1; }

  .testimonial {
    position: absolute; right: 49px; top: 574px; width: 720px;
    text-align: right; color: var(--white);
    font-size: 16px; line-height: 21.5px; font-weight: 500; letter-spacing: 0.55px;
    text-shadow: 0 1px 2px rgba(0,0,0,0.3);
  }
  .testimonial p + p { margin-top: 21px; }
  .testimonial .attribution { margin-top: 20px; }

  .accent-band { position: absolute; left: 0; top: 786px; width: 849px; height: 30px; background: var(--brand-blue); }
  .accent-band::after { content: ""; position: absolute; right: 0; top: 0; width: 49px; height: 30px; background: var(--brand-orange); }

  .feature-panel { position: absolute; left: 0; top: 816px; width: 849px; height: 384px; background: var(--brand-red); color: var(--white); }
  .headline {
    position: absolute; left: 50px; top: 35px; width: 780px;
    font-weight: 800; font-size: 33px; line-height: 40.5px; text-transform: uppercase; letter-spacing: 0.3px;
  }
  .feature-list {
    position: absolute; left: 50px; top: 196px; list-style: none;
    font-family: "Open Sans", sans-serif; font-weight: 700; font-size: 25.5px; line-height: 35.7px;
  }
</style>
</head>
<body>
<main class="brochure">
  <div class="hero-photo" role="img" aria-label="Lifestyle photograph: a traveller checking hotel occupancy on a smartphone outdoors, city street and trees behind"></div>

  <div class="brand">
    <span class="brand-dot"></span>
    <span class="brand-name">tidewell</span>
  </div>

  <blockquote class="testimonial">
    <p>We travel a lot and want to be able to see how the occupancy is at anytime.<br>We wanted a technology which could connect our HO to property and also<br>help us manage multiple properties.</p>
    <p>With tidewell adoption not only have we streamlined our operations but<br>also seen a 20% jump in occupancy</p>
    <p class="attribution">Tomov –MD, K-Lodging</p>
  </blockquote>

  <div class="accent-band"></div>

  <section class="feature-panel">
    <h1 class="headline">Hospitality solution that enables<br>operational excellence and<br>widens customer reach</h1>
    <ul class="feature-list">
      <li>A truly Integrated Solution</li>
      <li>Manages Distributed Operational Work-flows</li>
      <li>Inventory Distributions, Sales and Marketing</li>
      <li>Strategic Planning /Reporting and Management</li>
    </ul>
  </section>
</main>
</body>
</html>
```